Scented Candle Company Sticker Design for Packaging

We need a Sticker design for our various scented candle packages. Our handmade candles incorperate hand crafted Chiyogami Paper imported from Japan, which is wrapped around the jar. Each of the scents have different papers assigned to them and although we would like a general design in which the text can be changed according to each scent we would also like if the beautiful Japanese paper designs could be subtly incorporated in the design.

We want the the text of the sticker and logo of our company to be printed in gold foil once printed and our featured logo image is of a Dogwood tree. We think that perhaps the inclusion of dogwood blossom/s might look nice in the design but is not a must have!

We are fond of the delicate and classic print designs and etching designs. We would also like the design to be in a portrait rectangle that is closer in the shape of a square/ or not too long of a rectangle, and, would like to have a boarder on the edge of the sticker (this could incorporate the blossom if you wish, I have attached an image for reference/ inspiration) but we are after something much more simplistic and draws less attention to the eye and connected in the boarder.

Our brand is elegant and classic and we would like to be in keeping with our style. We have attached some images of the candles and our logo for inspiration, we do not want the stickers for the candle themselves but rather to place on the packaging.

Ive left some information for one of the candle scents for this design but once again I would like to reiterate that the design should allow for interchangeable titles for the other fragrances.

Velvet Harbour Dusk(in smaller writing).
Velvet Harbour Dusk, Orange blossom, cinnamon.

Our candles are hand made in Australia and a made from 100% soy wax and we would like to to be presented on the label.

I would like to mention again that we are looking for an elegant and classic design. We are looking for a simplistic design/layout that also focuses on the fine details. It should be striking but also not overbearing with an air of sophistication with minimal to no use of colours in encouraged.

I have also attached a font that is matched to the "candle co." underneath the tree in the logo.
Updates

I only just posted the design request, but first created the brief on the 2nd. I would like more time for the designers to both see my review and have an adequate amount of time to work on the project.

Target Market(s)

Up Market Shoppers.

Font styles to use
Script
Other font styles liked:
• Acorn

Colors
fbfbfb

Requirements
Must have
• Logo on the sticker.
Nice to have
• Nice to have a dogwood blossom incorporated into the boarder but must be simplistic as it doesn't want to be the main focus of the sticker
Should not have
• Photographs in the sticker design. Must be graphic design. No to little colour.

```html
<!DOCTYPE html>
<html lang="en">
<head>
<meta charset="utf-8">
<title>Larchmere Candle Co. — Velvet Harbour Dusk Label</title>
<link href="https://fonts.googleapis.com/css2?family=Cinzel:wght@400;600&family=Arimo:wght@400&display=swap" rel="stylesheet">
<style>
  :root {
    --page: #fbfbfb;
    --label-light: #f4f4f4;
    --label-mid: #d9d9d9;
    --label-dark: #b9b9b9;
    --label-edge: #8e8e8e;
    --frame: #7a7a7a;
    --ink: #3a3a3a;
    --title: #8a7a5c;
    --rule: #a8a8a8;
    --ornament-a: #d2d2d2;
    --ornament-b: #efefef;
  }
  html, body {
    margin: 0;
    padding: 0;
    width: 1200px;
    height: 1200px;
    overflow: hidden;
    background: var(--page);
  }
  .canvas {
    position: relative;
    width: 1200px;
    height: 1200px;
    background: var(--page);
  }
  .label {
    position: absolute;
    left: 200px;
    top: 140px;
    width: 800px;
    height: 920px;
    box-sizing: border-box;
    border: 2px solid var(--label-edge);
    background: linear-gradient(100deg, var(--label-mid) 0%, var(--label-light) 35%, var(--label-light) 60%, var(--label-dark) 100%);
  }
  .label-frame {
    position: absolute;
    left: 100px;
    right: 113px;
    top: 143px;
    bottom: 102px;
    border: 2px solid var(--frame);
    background: linear-gradient(100deg, #e6e6e6 0%, #f7f7f7 40%, #f2f2f2 70%, #dedede 100%);
  }
  .blossom-branch {
    position: absolute;
    right: 40px;
    top: 16px;
    width: 150px;
    height: 560px;
    border-radius: 45% 12% 50% 50% / 20% 6% 60% 60%;
    background: linear-gradient(180deg, var(--ornament-a) 0%, var(--ornament-b) 70%, rgba(239,239,239,0) 100%);
    opacity: 0.7;
    z-index: 1;
  }
  .brand, .scent, .details { z-index: 2; }
  .brand {
    position: absolute;
    left: 0;
    right: 0;
    top: 58px;
    text-align: center;
    color: var(--ink);
  }
  .brand-mark {
    display: inline-block;
    width: 34px;
    height: 34px;
    border-radius: 50%;
    background: var(--ink);
    margin-bottom: 10px;
  }
  .brand-name {
    font-family: "Cinzel", serif;
    font-weight: 600;
    font-size: 22px;
    letter-spacing: 4px;
    line-height: 1.1;
  }
  .brand-sub {
    font-family: "Cinzel", serif;
    font-weight: 600;
    font-size: 12px;
    letter-spacing: 4px;
    line-height: 1.1;
  }
  .scent {
    position: absolute;
    left: 22px;
    right: 22px;
    top: 190px;
    text-align: center;
  }
  .scent-title {
    font-family: "Cinzel", serif;
    font-weight: 400;
    font-size: 34px;
    letter-spacing: 1px;
    color: var(--title);
    margin: 0 0 8px;
  }
  .scent-rule {
    height: 2px;
    background: var(--rule);
  }
  .details {
    position: absolute;
    left: 0;
    right: 0;
    top: 430px;
    text-align: center;
    font-family: "Arimo", sans-serif;
    font-size: 28px;
    color: var(--ink);
    line-height: 1;
  }
  .details p { margin: 0 0 56px; }
</style>
</head>
<body>
<main class="canvas">
  <section class="label" aria-label="Candle packaging label">
    <div class="blossom-branch" role="img" aria-label="Fine etched blossom branch trailing down the top right corner of the label"></div>
    <div class="label-frame">
      <div class="brand">
        <span class="brand-mark"></span>
        <div class="brand-name">LARCHMERE</div>
        <div class="brand-sub">CANDLE CO.</div>
      </div>
      <div class="scent">
        <h1 class="scent-title">VELVET HARBOUR DUSK</h1>
        <div class="scent-rule"></div>
      </div>
      <div class="details">
        <p>100% soy wax</p>
        <p>Hand made in Australia</p>
      </div>
    </div>
  </section>
</main>
</body>
</html>
```